Business Card

We are looking to re-create our business card. Attached is the company logo. we would like it to be back and front. for example one side with the persons information and the other side with the company logo. Be as creative as you would like but also keep in mind, we are a Health Insurance company and we need to look professional as well.
Industry/Entity Type
Business

```html
<!DOCTYPE html>
<html lang="en">
<head>
<meta charset="utf-8">
<title>Harbor Wellness Group — Business Card</title>
<link rel="stylesheet" href="https://fonts.googleapis.com/css2?family=Source+Sans+3:wght@400;700&display=swap">
<style>
  :root {
    --backdrop: #76696a;
    --card: #333334;
    --card-edge: #1f1f20;
    --brand-blue: #5b9bd8;
    --sky: #8cb6e4;
    --sand: #c9b3a6;
    --mist: #dcdde3;
    --mark-grey: #b9b5b3;
    --contact: #d9d9d9;
  }
  * { margin: 0; padding: 0; box-sizing: border-box; }
  html, body {
    width: 1200px; height: 857px; overflow: hidden;
    background: var(--backdrop);
    font-family: "Source Sans 3", Arial, sans-serif;
  }
  .sheet {
    width: 1200px; height: 857px;
    display: flex; align-items: center; justify-content: center; gap: 40px;
  }
  .card {
    position: relative;
    width: 520px; height: 300px;
    background: var(--card);
    overflow: hidden;
    box-shadow: 0 2px 0 var(--card-edge), 0 14px 30px rgba(0,0,0,.25);
  }
  .card__art { position: absolute; inset: 0; width: 100%; height: 100%; }
  .contact {
    position: absolute;
    color: var(--contact);
    font-size: 15px; line-height: 22px; letter-spacing: .2px;
  }
  .card--back .contact { left: 110px; top: 96px; text-align: center; }
  .card--front .contact { right: 52px; bottom: 62px; text-align: left; }
  .identity {
    position: absolute; left: 96px; top: 128px;
    display: flex; align-items: center; height: 80px;
  }
  .identity__mark {
    color: var(--mark-grey);
    font-weight: 700; font-size: 36px; letter-spacing: -1px;
    padding-right: 16px;
  }
  .identity__rule {
    width: 1.5px; height: 76px; background: var(--sand);
  }
  .identity__name {
    color: var(--brand-blue);
    font-weight: 700; font-size: 24px;
    padding-left: 14px; margin-top: -26px;
  }
</style>
</head>
<body>
<main class="sheet">

  <section class="card card--back" aria-label="Card back">
    <svg class="card__art" viewBox="0 0 520 300" aria-hidden="true">
      <defs>
        <linearGradient id="backSweep" x1="0" y1="0" x2="1" y2="1">
          <stop offset="0" stop-color="#e6e6ea"/>
          <stop offset="1" stop-color="#c7ab9b"/>
        </linearGradient>
      </defs>
      <path d="M405 0 L520 0 L520 300 L500 300 C498 170 470 70 405 0 Z" fill="url(#backSweep)"/>
      <path d="M438 0 L520 0 L520 300 L510 300 C510 180 490 70 438 0 Z" fill="var(--sand)" opacity=".75"/>
    </svg>
    <p class="contact">mira@harborwellness.example<br>000 - 1XXXXX xx &nbsp;000 - XXXx - XXX</p>
  </section>

  <section class="card card--front" aria-label="Card front">
    <svg class="card__art" viewBox="0 0 520 300" aria-hidden="true">
      <defs>
        <linearGradient id="frontSweep" x1="0" y1="0" x2="0" y2="1">
          <stop offset="0" stop-color="#c9ad9d"/>
          <stop offset=".55" stop-color="#a9a9c0"/>
          <stop offset="1" stop-color="#8cb6e4"/>
        </linearGradient>
        <linearGradient id="cornerSweep" x1="0" y1="0" x2="1" y2="1">
          <stop offset="0" stop-color="#dfe2ea"/>
          <stop offset="1" stop-color="#8cb6e4"/>
        </linearGradient>
      </defs>
      <path d="M0 0 L22 0 C50 120 100 230 200 300 L0 300 Z" fill="url(#frontSweep)"/>
      <path d="M0 90 C30 190 90 260 175 300 L0 300 Z" fill="var(--sky)" opacity=".7"/>
      <path d="M0 170 C40 240 90 275 140 300 L0 300 Z" fill="var(--mist)" opacity=".35"/>
      <path d="M430 0 L520 0 L520 58 C485 42 455 22 430 0 Z" fill="url(#cornerSweep)"/>
    </svg>
    <div class="identity">
      <span class="identity__mark">HWG</span>
      <span class="identity__rule"></span>
      <span class="identity__name">Harbor Wellness Group</span>
    </div>
    <p class="contact">mira@harborwellness.example<br>000 - 1XXXXX xx &nbsp;000 - XXXx - XXX</p>
  </section>

</main>
</body>
</html>
```